Merry Christmas & A Happy New Year

We need a Greeting Card for this year's Christmas & New Year.

We are a company dealing in the Mechanical Engineering & Manufacturing Industry. Example: Aero Space, Oil & Gas, Marine, etc…

Requirements
Must have
• Company Logo

```html
<!DOCTYPE html>
<html lang="en">
<head>
<meta charset="utf-8">
<title>Season's Greetings – Kestrel Works</title>
<link href="https://fonts.googleapis.com/css2?family=Lobster&display=swap" rel="stylesheet">
<style>
  :root {
    --sky-top: #e4e9ee;
    --sky-mid: #d9e0e7;
    --sky-low: #e6eaef;
    --ring: #ffffff;
    --ring-shadow: #aeb8c3;
    --crimson: #b0123f;
    --crimson-deep: #7e0a2b;
    --flake-white: #ffffff;
    --flake-shade: #b4bfcb;
  }
  html, body {
    margin: 0;
    padding: 0;
    overflow: hidden;
    background: var(--sky-mid);
  }
  .greeting-card {
    position: relative;
    width: 771px;
    height: 1200px;
    overflow: hidden;
    background:
      radial-gradient(ellipse 420px 160px at 120px 790px, rgba(150,165,180,0.35), transparent 70%),
      linear-gradient(180deg, var(--sky-top) 0%, var(--sky-mid) 55%, var(--sky-low) 100%);
    font-family: "Lobster", cursive;
  }
  .snowflake-ornaments,
  .greeting-ring {
    position: absolute;
    inset: 0;
    width: 771px;
    height: 1200px;
  }
  .greeting-message {
    position: absolute;
    left: 190px;
    top: 338px;
    width: 400px;
    margin: 0;
    text-align: center;
    font-family: "Lobster", cursive;
    font-weight: 400;
    font-size: 76px;
    line-height: 75px;
    color: var(--crimson);
    text-shadow: 0 2px 0 var(--crimson-deep);
  }
  .company-mark {
    position: absolute;
    left: 0;
    top: 1030px;
    width: 771px;
    display: flex;
    justify-content: center;
    align-items: center;
    gap: 16px;
  }
  .company-mark .mark-dot {
    width: 48px;
    height: 48px;
    border-radius: 50%;
    background: var(--crimson);
  }
  .company-mark .company-name {
    font-family: "Lobster", cursive;
    font-size: 54px;
    line-height: 70px;
    color: var(--crimson);
  }
</style>
</head>
<body>
<main class="greeting-card">
  <svg class="snowflake-ornaments" viewBox="0 0 771 1200" role="img" aria-label="Paper-cut white snowflake ornaments clustered around the ring, with small snowflakes scattered across the card">
    <defs>
      <radialGradient id="flake-fill" cx="50%" cy="45%" r="55%">
        <stop offset="0%" stop-color="var(--flake-white)"/>
        <stop offset="70%" stop-color="#f4f6f9"/>
        <stop offset="100%" stop-color="#e2e7ed"/>
      </radialGradient>
      <filter id="paper-shadow" x="-30%" y="-30%" width="160%" height="160%">
        <feDropShadow dx="-4" dy="6" stdDeviation="6" flood-color="var(--flake-shade)" flood-opacity="0.8"/>
      </filter>
    </defs>
    <g filter="url(#paper-shadow)" fill="url(#flake-fill)">
      <!-- upper-left cluster -->
      <circle cx="128" cy="245" r="82"/>
      <circle cx="262" cy="238" r="74"/>
      <circle cx="378" cy="184" r="40"/>
      <circle cx="468" cy="160" r="16"/>
      <circle cx="430" cy="212" r="22"/>
      <circle cx="122" cy="410" r="112"/>
      <circle cx="28" cy="288" r="24"/>
      <circle cx="98" cy="580" r="32"/>
      <circle cx="132" cy="650" r="20"/>
      <circle cx="72" cy="512" r="14"/>
      <!-- right cluster -->
      <circle cx="590" cy="420" r="36"/>
      <circle cx="630" cy="530" r="92"/>
      <circle cx="735" cy="575" r="50"/>
      <circle cx="730" cy="480" r="28"/>
      <circle cx="690" cy="420" r="18"/>
      <circle cx="648" cy="745" r="112"/>
      <circle cx="670" cy="635" r="34"/>
      <circle cx="730" cy="820" r="34"/>
      <!-- lower band -->
      <circle cx="488" cy="840" r="60"/>
      <circle cx="400" cy="828" r="34"/>
      <circle cx="345" cy="878" r="38"/>
      <circle cx="295" cy="820" r="24"/>
      <circle cx="220" cy="825" r="20"/>
      <circle cx="560" cy="868" r="24"/>
      <circle cx="455" cy="760" r="20"/>
      <circle cx="112" cy="828" r="20"/>
      <circle cx="176" cy="798" r="12"/>
    </g>
    <g fill="var(--flake-white)" opacity="0.85">
      <circle cx="620" cy="90" r="6"/><circle cx="700" cy="170" r="5"/><circle cx="560" cy="250" r="5"/>
      <circle cx="640" cy="300" r="6"/><circle cx="40" cy="660" r="5"/><circle cx="60" cy="860" r="5"/>
      <circle cx="150" cy="880" r="4"/><circle cx="255" cy="860" r="5"/><circle cx="615" cy="880" r="5"/>
      <circle cx="250" cy="840" r="4"/><circle cx="520" cy="920" r="4"/><circle cx="22" cy="720" r="4"/>
    </g>
  </svg>

  <svg class="greeting-ring" viewBox="0 0 771 1200" aria-hidden="true">
    <circle cx="377" cy="499" r="240" fill="none" stroke="var(--ring-shadow)" stroke-opacity="0.4" stroke-width="34" transform="translate(-8 10)"/>
    <circle cx="377" cy="499" r="226" fill="none" stroke="var(--ring)" stroke-width="30"/>
  </svg>

  <h1 class="greeting-message">Merry<br>Christmas<br>and Happy<br>New Year</h1>

  <div class="company-mark">
    <span class="mark-dot"></span>
    <span class="company-name">Kestrel Works</span>
  </div>
</main>
</body>
</html>
```